Business card & stationery for audio visual & security system installation company
Audio visual & security system installations
I need double sided standard sized Business Card [3.5" x 2"]
Up to the designer
Professional
Teodor Malsk
Suite 418, 6 -10 Quenby Street,
Elwood Vale, VIC 3187
teodor@plenvo.com.au
www.plenvo.com.au
Master Cabler No - K519207
Logo on the front
Logo on the back

```html
<!DOCTYPE html>
<html lang="en">
<head>
<meta charset="utf-8">
<title>Plenvo Business Card</title>
<link rel="stylesheet" href="https://fonts.googleapis.com/css2?family=Open+Sans:wght@400;600;800&display=swap">
<style>
  :root {
    --backdrop: #e9e7e4;
    --card: #ffffff;
    --brand-red: #d9161c;
    --ink: #555555;
    --ink-soft: #8a8a8a;
    --rule: #d6d6d6;
  }
  * { margin: 0; padding: 0; box-sizing: border-box; }
  html, body { width: 1200px; height: 629px; overflow: hidden; }
  body {
    background: var(--backdrop);
    font-family: "Open Sans", Arial, sans-serif;
    position: relative;
  }
  .card {
    position: absolute;
    top: 160px;
    width: 540px;
    height: 309px;
    background: var(--card);
    box-shadow: 0 6px 18px rgba(0,0,0,0.12);
  }
  .card--front { left: 40px; }
  .card--back { left: 620px; }

  .brand {
    display: flex;
    align-items: center;
    gap: 12px;
    color: var(--brand-red);
    font-weight: 800;
    letter-spacing: -1px;
    white-space: nowrap;
  }
  .brand__dot {
    width: 0.55em; height: 0.55em;
    border-radius: 50%;
    background: var(--brand-red);
  }
  .card--front .brand {
    position: absolute;
    left: 50%; top: 50%;
    transform: translate(-50%, -50%);
    font-size: 78px;
  }
  .card--back .brand {
    position: absolute;
    left: 52px; top: 60px;
    font-size: 52px;
  }

  .holder {
    position: absolute;
    left: 52px; top: 168px;
    width: 220px;
  }
  .holder__name {
    color: var(--brand-red);
    font-weight: 600;
    font-size: 15px;
    margin-bottom: 22px;
  }
  .holder__address {
    color: var(--ink-soft);
    font-size: 11.5px;
    line-height: 1.55;
  }

  .divider {
    position: absolute;
    left: 288px; top: 82px;
    width: 1px; height: 180px;
    background: var(--rule);
  }

  .contacts {
    position: absolute;
    left: 302px; top: 80px;
    list-style: none;
  }
  .contacts li {
    display: flex;
    align-items: center;
    gap: 10px;
    height: 24px;
    color: var(--ink);
    font-size: 12px;
    white-space: nowrap;
  }
  .contacts svg { width: 15px; height: 15px; flex: none; }
</style>
</head>
<body>
  <section class="card card--front">
    <div class="brand"><span class="brand__dot"></span>Plenvo</div>
  </section>

  <section class="card card--back">
    <div class="brand"><span class="brand__dot"></span>Plenvo</div>

    <div class="holder">
      <p class="holder__name">Teodor Malsk</p>
      <p class="holder__address">Suite 418, 6 -10 Quenby Street,<br>Elwood Vale, VIC 3187</p>
    </div>

    <div class="divider"></div>

    <ul class="contacts">
      <li>
        <svg viewBox="0 0 16 16"><circle cx="8" cy="8" r="8" fill="#d9161c"/><path d="M5.3 4.2l1.4-.3.8 1.9-.9.7a5 5 0 0 0 2.4 2.4l.7-.9 1.9.8-.3 1.4c-3.6.3-6.3-2.4-6-6z" fill="#fff"/></svg>
        02 9471 5308
      </li>
      <li>
        <svg viewBox="0 0 16 16"><circle cx="8" cy="8" r="8" fill="#d9161c"/><rect x="5.5" y="3.5" width="5" height="9" rx="1" fill="#fff"/><rect x="6.3" y="4.6" width="3.4" height="5.6" fill="#d9161c"/></svg>
        0418 362 905
      </li>
      <li>
        <svg viewBox="0 0 16 16"><circle cx="8" cy="8" r="8" fill="#d9161c"/><rect x="4" y="7" width="8" height="4.5" rx=".6" fill="#fff"/><rect x="5.5" y="4" width="5" height="3" fill="#fff"/></svg>
        02 9471 5319
      </li>
      <li>
        <svg viewBox="0 0 16 16"><circle cx="8" cy="8" r="8" fill="#d9161c"/><rect x="4" y="5" width="8" height="6" rx=".6" fill="#fff"/><path d="M4.3 5.4L8 8.3l3.7-2.9" stroke="#d9161c" stroke-width="1" fill="none"/></svg>
        teodor@plenvo.com.au
      </li>
      <li>
        <svg viewBox="0 0 16 16"><circle cx="8" cy="8" r="8" fill="#d9161c"/><circle cx="8" cy="8" r="4" stroke="#fff" stroke-width="1.1" fill="none"/><path d="M4 8h8M8 4c-2 2.4-2 5.6 0 8M8 4c2 2.4 2 5.6 0 8" stroke="#fff" stroke-width="1" fill="none"/></svg>
        www.plenvo.com.au
      </li>
    </ul>
  </section>
</body>
</html>
```